Web Design Project

We need a web design for a legal firm based in Sydney, Australia. Our main clients are small businesses, accountants and entrepreneurs. We help our clients deal with commercial disputes and litigation.
In terms of the site design, we would like the site to appear professional, clean and easy to navigate however we would like it to be slightly more creative than the average legal website.
Legal Sites we like:
http://www.kvr.com.au/
http://www.pennystacker.com/
http://www.tiru.com/
Non-Legal Sites we like:
http://www.plevna.com/index-b.html
http://www.brimworth.com/
http://www.quillory.com/
Sites we don't like:
http://www.oregonlevyfixers.com/
We have listed below some possible colour palettes for the site:
http://www.huefanciers.com/palette/74162/Legal_Man
http://www.huefanciers.com/palette/651375/Legal_Transplant
http://www.huefanciers.com/palette/199581/Legal_Notice
Site design elements we like:
Large Footer (with newsletter sign up form)
Full screen (postwren.com, brimworth.com)
Customised Social Media icons that fit in with the style of our website
Slider
We need the following templates created:
Home Page
General Content Page
Blog
Target Market(s)
Small to Medium Sized Businesses and Entrepreneurs
Industry/Entity Type
Legal
Look and feel

```html
<!DOCTYPE html>
<html lang="en">
<head>
<meta charset="utf-8">
<title>Harrow &amp; Vale Lawyers – The Insights Blog</title>
<link rel="stylesheet" href="https://fonts.googleapis.com/css2?family=Open+Sans:ital,wght@0,300;0,400;0,600;0,700;1,400;1,600&display=swap">
<style>
:root{
  --sky-top:#5aa9dc;
  --sky-bottom:#bfe0f3;
  --nav:#8fd0d6;
  --nav-line:#6fbcc5;
  --teal:#5fb8c4;
  --teal-light:#8ccfd6;
  --teal-dark:#3e9fae;
  --cream:#eef0d9;
  --cream-dark:#e2e5cb;
  --footer:#e4e6d1;
  --ink:#3c3c3c;
  --image:#f4f5e4;
  --link-blue:#1f5fa6;
  --white:#ffffff;
}
*{box-sizing:border-box;margin:0;padding:0}
html,body{width:731px;height:1200px;overflow:hidden}
body{position:relative;background:var(--white);font-family:"Open Sans",Arial,sans-serif;color:var(--ink)}
.abs{position:absolute}

/* header */
.site-header{left:0;top:0;width:731px;height:77px;background:linear-gradient(180deg,var(--sky-top),var(--sky-bottom))}
.brand{left:60px;top:17px;width:105px;height:45px;background:var(--white);display:flex;align-items:center;justify-content:center;font-size:10px;font-weight:600;color:#333;white-space:nowrap}
.main-nav{left:165px;top:17px;width:505px;height:45px;background:var(--nav);border-bottom:2px solid var(--nav-line);display:flex;align-items:center;justify-content:center;font-size:11px;color:#3f7f88}

/* sidebar */
.widget{left:73px;width:140px}
.blog-badge{top:95px;height:78px;background:var(--cream)}
.blog-badge .name{left:0;top:22px;width:140px;text-align:center;font-size:11px;font-weight:600;color:#333}
.blog-badge .title{left:0;top:53px;width:140px;text-align:center;font-size:11px;color:var(--teal-dark)}
.company-card{top:180px;height:115px;background:#e6e6e6}
.company-card .card{left:2px;top:3px;width:136px;height:92px;background:var(--white);border:1px solid #cfcfcf;padding:10px 7px;font-family:Arial,sans-serif}
.company-card h3{font-size:10px;color:var(--link-blue);font-weight:700;margin-bottom:6px}
.company-card p{font-size:6.4px;line-height:8px;color:#222;margin-bottom:5px}
.company-card .foot{left:3px;top:97px;width:134px;font-size:6px;line-height:8px;color:#555;font-family:Arial,sans-serif}
.company-card .foot b{color:var(--link-blue);font-weight:400}
.promo{background:var(--cream-dark)}
.promo h4{left:17px;font-size:9.5px;line-height:11px;font-weight:400;color:#555}
.promo p{left:17px;font-size:7.3px;line-height:9px;color:#555}
.promo .art{width:54px;height:62px;background:linear-gradient(160deg,#ffffff,#d9dcc8);border-radius:2px}
.promo .btn{left:6px;width:128px;height:24px;background:var(--teal);color:var(--white);font-size:8.5px;display:flex;align-items:center;justify-content:center;gap:8px}
.feed-links{left:90px;top:559px;font-size:7px;color:#555;line-height:17px;list-style:none}
.feed-links li{display:flex;align-items:center;gap:6px}
.feed-links .ico{width:9px;height:9px;border-radius:1px}
.select{top:618px;height:20px;background:#e8e8e8;font-size:7.3px;color:#555;padding:5px 0 0 16px}
.select svg{position:absolute;right:9px;top:8px}
.widget-head{height:30px;background:var(--teal-light);color:var(--white);font-size:11.5px;font-weight:400;padding:7px 0 0 16px}
.popular-list{list-style:none}
.popular-list li{position:absolute;left:0;width:140px;font-size:7.8px;line-height:10px;color:#4f8b94;padding:0 30px 0 16px}
.popular-list li::before{content:"";position:absolute;left:9px;top:4px;width:3px;height:3px;border-radius:50%;background:currentColor}
.popular-list .active{background:var(--teal);border:1px solid var(--teal-dark);color:var(--white);height:22px;line-height:20px;padding-right:0}
.popular-list .active::before{top:9px}
.bars{top:838px;width:140px}
.bar{position:absolute;left:0;height:16px;background:#9dd6dc;border:1px solid #7cc6ce;font-size:8px;line-height:14px;color:#3f6f76;padding-left:15px;white-space:nowrap}
.bar-value{position:absolute;right:12px;font-size:8px;line-height:16px;color:#555}

/* posts */
.post{left:250px;width:407px}
.post h2{position:absolute;left:17px;top:0;font-size:16px;line-height:22px;font-weight:300;color:#333;white-space:nowrap}
.post .rule{position:absolute;left:0;top:27px;width:407px;height:2px;background:var(--teal-light)}
.meta{position:absolute;left:17px;top:34px;width:390px;height:12px;font-size:7px;color:#666;display:flex;align-items:center;white-space:nowrap}
.meta .cat{color:var(--teal-dark);font-style:italic}
.meta i{font-weight:600}
.meta .right{margin-left:auto;display:flex;align-items:center;gap:3px}
.share{border:1px solid #c4c4c4;background:#f4f4f4;font-size:6.5px;padding:0 3px;line-height:10px;color:#333;font-weight:600}
.count{border:1px solid #c4c4c4;background:var(--white);font-size:6.5px;padding:0 3px;line-height:10px;color:#333}
.count.blue{color:#2b6aa8}
.post .image{position:absolute;left:12px;top:53px;width:395px;height:100px;background:var(--image);display:flex;align-items:center;justify-content:center;font-size:24px;font-weight:300;color:#e0e3cc;letter-spacing:1px}
.post .body{position:absolute;left:18px;top:158px;width:385px;font-size:7.3px;line-height:11px;color:#444}
.post .body p{margin-bottom:10px}
.read-more{display:block;width:62px;height:16px;background:var(--teal);color:var(--white);font-size:7.3px;font-weight:600;text-align:center;line-height:16px}

/* footer */
.site-footer{left:0;top:1057px;width:731px;height:143px;background:var(--footer)}
.site-footer h5{position:absolute;top:18px;font-size:11px;font-weight:400;color:#666}
.divider{position:absolute;top:15px;width:1px;height:118px;background:#cfd2bc}
.assoc-text{left:80px;top:44px;width:78px;font-size:7.2px;line-height:10px;color:#444}
.partner{font-size:6px;font-weight:700;color:#444;text-align:center;width:40px}
.partner span{display:block;margin:0 auto 2px;width:14px;height:14px;border-radius:50%}
.newsletter h6{position:absolute;left:255px;top:44px;font-size:8.5px;font-weight:600;color:#333}
.field{position:absolute;left:255px;width:153px;height:16px;background:#f5f6ea;font-size:6.8px;line-height:16px;color:#777;padding-left:11px}
.signup{left:255px;top:99px;width:49px;height:15px;background:var(--teal);color:var(--white);font-size:7.3px;text-align:center;line-height:15px}
.find-us{left:328px;top:101px;font-size:7px;color:#333}
.find-us b{font-weight:700}
.contact{font-size:7.3px;line-height:10.5px;color:#333}
.contact b{font-weight:600;font-size:8px}
</style>
</head>
<body>

<header class="site-header abs">
  <div class="brand abs">Harrow &amp; Vale</div>
  <nav class="main-nav abs">Connect</nav>
</header>

<aside>
  <section class="widget blog-badge abs">
    <p class="name abs">Harrow &amp; Vale</p>
    <p class="title abs">The Insights Blog</p>
  </section>

  <section class="widget company-card abs">
    <div class="card abs">
      <h3>Harrow &amp; Vale Lawyers</h3>
      <p>Harrow &amp; Vale is a Sydney law firm that advises small and medium sized enterprises (SMEs), investors and entrepreneurs.</p>
      <p>The firm is...</p>
      <p>Sydney. 2 Employees</p>
    </div>
    <p class="foot abs"><b>Sign in</b> to see how you're connected to Harrow &amp; Vale Lawyers</p>
  </section>

  <section class="widget promo abs" style="top:306px;height:116px">
    <h4 class="abs" style="top:10px">Get to know<br><span style="font-size:13px">us...</span></h4>
    <p class="abs" style="top:41px">Register for<br>local events,<br>webinars &amp;<br>product demos.</p>
    <div class="art abs" role="img" aria-label="Illustration of a registration form with a pen" style="left:80px;top:8px"></div>
    <div class="btn abs" style="top:85px">Register for an event
      <svg width="12" height="9" viewBox="0 0 12 9"><path d="M0 4.5h10M7 1l3.5 3.5L7 8" stroke="#fff" stroke-width="1.4" fill="none"/></svg></div>
  </section>

  <section class="widget promo abs" style="top:433px;height:116px">
    <h4 class="abs" style="top:12px">Free Whitepaper...</h4>
    <p class="abs" style="top:31px">10 metrics you<br>can't get from<br>your billing<br>system</p>
    <div class="art abs" role="img" aria-label="Illustration of stacked documents with a bookmark ribbon" style="left:70px;top:30px;height:52px"></div>
    <div class="btn abs" style="top:86px">View today
      <svg width="12" height="9" viewBox="0 0 12 9"><path d="M0 4.5h10M7 1l3.5 3.5L7 8" stroke="#fff" stroke-width="1.4" fill="none"/></svg></div>
  </section>

  <ul class="feed-links abs">
    <li><span class="ico" style="background:#f28c1e"></span>All Blogs RSS Feed</li>
    <li><svg class="ico" viewBox="0 0 9 9"><rect x=".5" y="1.5" width="8" height="6" fill="#fff" stroke="#888"/><path d="M.5 1.5l4 3.5 4-3.5" stroke="#888" fill="none"/></svg>All Blogs Email Subscription</li>
    <li><span class="ico" style="background:#b4864a"></span>All Blogs Archives</li>
  </ul>

  <div class="widget select abs">Category Archive..
    <svg width="7" height="5" viewBox="0 0 7 5"><path d="M0 0h7L3.5 5z" fill="#bbb"/></svg></div>

  <section class="widget abs" style="top:651px">
    <h4 class="widget-head">Popular Posts</h4>
    <ul class="popular-list">
      <li class="active" style="top:37px">Lorem ipsum dolor sit amet</li>
      <li style="top:62px">Donec condimentum, nisi ut sagittis fringilla, sit leo interdum ante</li>
      <li style="top:104px">Etiam iaculis, ipsum vel placerat commodo</li>
    </ul>
  </section>

  <section class="widget abs" style="top:798px">
    <h4 class="widget-head">Popular Posts</h4>
  </section>
  <div class="widget bars abs">
    <div class="bar" style="top:0;width:97px">Lorem ipsum</div><span class="bar-value" style="top:0">146</span>
    <div class="bar" style="top:18px;width:84px">Dolor sit</div><span class="bar-value" style="top:18px">126</span>
    <div class="bar" style="top:36px;width:79px">Amet</div><span class="bar-value" style="top:36px">112</span>
    <div class="bar" style="top:54px;width:61px">Sagittis fringilla</div><span class="bar-value" style="top:54px">84</span>
    <div class="bar" style="top:72px;width:52px">Interdum ante</div><span class="bar-value" style="top:72px">72</span>
    <div class="bar" style="top:90px;width:31px">Etiam</div><span class="bar-value" style="top:90px">45</span>
  </div>
</aside>

<main>
  <article class="post abs" style="top:97px">
    <h2>Mauris quis dui sit amet leo venenatis interdum.</h2>
    <div class="rule"></div>
    <div class="meta"><span class="cat">Category</span>&nbsp;By&nbsp;<i>Name Surname</i>&nbsp;&nbsp;|&nbsp;&nbsp;July 12, 2012
      <span class="right"><svg width="8" height="7" viewBox="0 0 8 7"><path d="M0 0h8v5H3L1 7V5H0z" fill="#aaa"/></svg>&nbsp;<i>124</i>&nbsp;Comments&nbsp;&nbsp;<span class="share">Linkwell</span><span class="count blue">156</span>&nbsp;<span class="share">Chirper</span><span class="count">7</span></span></div>
    <div class="image" role="img" aria-label="Post image">IMAGE</div>
    <div class="body">
      <p>Aer, purus tortor eleifend sapien, non dignissim augue nulla at justo. <u>Duis fermentum leo ut</u> turpis molestie suscipit. Maecenas non mi et neque ultrices pharetra quis et est. Nam pulvinar vehicula risus, nec pellentesque massa hendrerit vitae. Curabitur pellentesque ultrices interdum. Nam interdum eros sed ligula gravida vel posuere libero volutpat. Donec et diam molestie elit pretium adipiscing et vitae nisl. Morbi in risus et massa lobortis viverra.</p>
      <p>Mauris quis dui sit amet leo venenatis interdum. Aenean ut dui vitae nisl suscipit volutpat. Nullam hendrerit magna vel tellus rutrum quis varius nulla placerat. In lobortis, urna quis luctus fringilla, risus tortor consequat nisi, sed ultricies purus mi at augue. Pellentesque enim ipsum, sodales in interdum at, convallis eget mi. Ut suscipit fringilla arcu, ut lacinia ante gravida eget. Donec mollis euismod odio, a tincidunt ante tincidunt at. Vestibulum a turpis quis arcu blandit vehicula.</p>
      <span class="read-more">Read more</span>
    </div>
  </article>

  <article class="post abs" style="top:421px">
    <h2>Mauris quis dui sit amet leo venenatis interdum.</h2>
    <div class="rule"></div>
    <div class="meta"><span class="cat">Category</span>&nbsp;By&nbsp;<i>Name Surname</i>&nbsp;&nbsp;|&nbsp;&nbsp;July 12, 2012
      <span class="right"><svg width="8" height="7" viewBox="0 0 8 7"><path d="M0 0h8v5H3L1 7V5H0z" fill="#aaa"/></svg>&nbsp;<i>124</i>&nbsp;Comments&nbsp;&nbsp;<span class="share">Linkwell</span><span class="count blue">156</span>&nbsp;<span class="share">Chirper</span><span class="count">7</span></span></div>
    <div class="image" role="img" aria-label="Post image">IMAGE</div>
    <div class="body">
      <p>Suspendisse at adipiscing ipsum. Cras sodales tincidunt adipiscing. Vivamus volutpat odio vel lectus suscipit ac varius eros ullamcorper. Quisque gravida justo vel sapien consequat tempus. Cras tincidunt, tortor et pretium hendrerit, purus nunc pretium tortor, eget vulputate lacus neque at libero. Curabitur scelerisque vehicula sem, facilisis consequat lacus commodo ut. Suspendisse placerat commodo leo, et consequat augue tempus in. Curabitur a felis risus.</p>
      <p>Vestibulum dignissim lectus in lectus pretium fringilla. Duis pellentesque eros vel ante posuere tincidunt vel ut libero. Morbi vitae urna est, eget auctor nibh. Fusce suscipit venenatis scelerisque. Aenean nisl leo, rutrum non dictum ut, tincidunt nec velit. Praesent ac vehicula quam. Nunc lobortis porta feugiat. Aenean sit amet posuere turpis. Nullam tincidunt metus a augue mollis ornare.</p>
      <span class="read-more">Read more</span>
    </div>
  </article>

  <article class="post abs" style="top:735px">
    <h2>Mauris quis dui sit amet leo venenatis interdum.</h2>
    <div class="rule"></div>
    <div class="meta"><span class="cat">Category</span>&nbsp;By&nbsp;<i>Name Surname</i>&nbsp;&nbsp;|&nbsp;&nbsp;July 12, 2012
      <span class="right"><svg width="8" height="7" viewBox="0 0 8 7"><path d="M0 0h8v5H3L1 7V5H0z" fill="#aaa"/></svg>&nbsp;<i>124</i>&nbsp;Comments&nbsp;&nbsp;<span class="share">Linkwell</span><span class="count blue">156</span>&nbsp;<span class="share">Chirper</span><span class="count">7</span></span></div>
    <div class="image" role="img" aria-label="Post image">IMAGE</div>
    <div class="body">
      <p>Suspendisse at adipiscing ipsum. Cras sodales tincidunt adipiscing. Vivamus volutpat odio vel lectus suscipit ac varius eros ullamcorper. Quisque gravida justo vel sapien consequat tempus. Cras tincidunt, tortor et pretium hendrerit, purus nunc pretium tortor, eget vulputate lacus neque at libero. Curabitur scelerisque vehicula sem, facilisis consequat lacus commodo ut. Suspendisse placerat commodo leo, et consequat augue tempus in. Curabitur a felis risus.</p>
      <p>Vestibulum dignissim lectus in lectus pretium fringilla. Duis pellentesque eros vel ante posuere tincidunt vel ut libero. Morbi vitae urna est, eget auctor nibh. Fusce suscipit venenatis scelerisque. Aenean nisl leo, rutrum non dictum ut, tincidunt nec velit. Praesent ac vehicula quam. Nunc lobortis porta feugiat. Aenean sit amet posuere turpis. Nullam tincidunt metus a augue mollis ornare.</p>
      <span class="read-more">Read more</span>
    </div>
  </article>
</main>

<footer class="site-footer abs">
  <h5 style="left:78px">Associations</h5>
  <p class="assoc-text abs">Lorem ipsum dolor sit amet, consectetur adipiscing elit. Morbi risus lorem, sollicitudin sed gravida non</p>
  <div class="partner abs" style="left:158px;top:45px"><span style="background:#2a5fa8"></span>Fizzco</div>
  <div class="partner abs" style="left:195px;top:45px"><span style="background:#c8202c"></span>Roovair</div>
  <div class="partner abs" style="left:158px;top:80px"><span style="background:#7a9f3a"></span>Panesoft</div>
  <div class="partner abs" style="left:195px;top:80px"><span style="background:#1d2c5a"></span>Lionport Air</div>
  <div class="divider" style="left:242px"></div>

  <h5 style="left:256px">Connect</h5>
  <div class="newsletter">
    <h6>Sign Up to Our Newsletter</h6>
    <div class="field" style="top:58px">Your name here..</div>
    <div class="field" style="top:77px">Your e-mail here..</div>
  </div>
  <div class="signup abs">Sign Up</div>
  <p class="find-us abs">Find us on <b>Linkwell</b></p>
  <div class="divider" style="left:419px"></div>

  <h5 style="left:431px">Contact us</h5>
  <p class="contact abs" style="left:431px;top:44px"><b>Company name</b><br>Address, lane 512/ 7C<br>Harbour town<br>5096310</p>
  <svg class="abs" style="left:536px;top:46px" width="14" height="14" viewBox="0 0 14 14"><path d="M3 1l2.5 3-1.5 1.5c.8 1.8 2.2 3.2 4 4L9.5 8 13 10.5 11.5 13C6 13 1 8 1 2.5z" fill="#9a9a8a"/></svg>
  <p class="contact abs" style="left:559px;top:45px"><b>Phone:</b><br>0417 55 203 96 148</p>
  <svg class="abs" style="left:536px;top:82px" width="14" height="10" viewBox="0 0 14 10"><rect width="14" height="10" fill="#9a9a8a"/><path d="M0 0l7 5.5L14 0" stroke="#e4e6d1" fill="none"/></svg>
  <p class="contact abs" style="left:559px;top:79px"><b>E-mail:</b><br>hello@harrowvale.com</p>
</footer>

</body>
</html>
```